Modern Lawfirm Business Card Design

We're looking for a business card to incorporate the newly created logo we had made.

Ideally looking for a law firm business card demonstrating, modern, minimalist, strong/bold design.

I'm open to any design honestly, but nothing "flashy".

Target Market(s)

Immigration law, family immigration, humanitarian, general legal

Industry/Entity Type

Law Firm

Contact Information for Business Card

Please use dummy information, name, street address, city, state, phone number, email, website.

Font styles to use
Serif
Sans Serif

Requirements
Must have
• Please use dummy information, name, street address, city, state, phone number, email, website.

```html
<!DOCTYPE html>
<html lang="en">
<head>
<meta charset="utf-8">
<title>Arcova Immigration Law – Business Card</title>
<link rel="stylesheet" href="https://fonts.googleapis.com/css2?family=Tinos:wght@400;700&display=swap">
<style>
  :root {
    --backdrop: #1d1e21;
    --card-white: #ffffff;
    --brand-blue: #1f4d8f;
    --brand-blue-light: #2a5ea6;
    --brand-blue-dark: #173f78;
    --ink-white: #ffffff;
    --ink-soft: #e3e9f3;
  }
  * { box-sizing: border-box; margin: 0; padding: 0; }
  html, body {
    width: 1200px;
    height: 900px;
    overflow: hidden;
    background: var(--backdrop);
    font-family: "Tinos", "Times New Roman", serif;
  }
  .canvas {
    position: relative;
    width: 1200px;
    height: 900px;
  }
  .card {
    position: absolute;
    width: 520px;
    height: 298px;
    box-shadow: 0 18px 40px rgba(0, 0, 0, 0.45);
  }
  .card--front {
    left: 90px;
    top: 150px;
    background: var(--card-white);
    display: flex;
    align-items: center;
    justify-content: center;
  }
  .card--back {
    left: 590px;
    top: 452px;
    background: radial-gradient(ellipse at 60% 40%, var(--brand-blue-light) 0%, var(--brand-blue) 55%, var(--brand-blue-dark) 100%);
    color: var(--ink-white);
  }
  .brand {
    display: flex;
    align-items: center;
    gap: 10px;
    color: var(--brand-blue);
    font-weight: 700;
  }
  .brand__square {
    width: 14px;
    height: 14px;
    background: currentColor;
  }
  .brand__text {
    display: flex;
    flex-direction: column;
    align-items: flex-start;
    line-height: 1;
  }
  .brand__name {
    font-size: 40px;
    letter-spacing: 1px;
    text-transform: uppercase;
  }
  .brand__tag {
    margin-top: 5px;
    font-size: 9.5px;
    letter-spacing: 5.2px;
    text-transform: uppercase;
  }
  .card--back .brand {
    color: var(--ink-white);
    position: absolute;
    right: 36px;
    top: 42px;
  }
  .card--back .brand__name { font-size: 34px; }
  .card--back .brand__tag { font-size: 8px; letter-spacing: 4.4px; }
  .contact {
    position: absolute;
    right: 36px;
    top: 118px;
    text-align: right;
    font-weight: 400;
  }
  .contact__name {
    font-size: 17px;
    letter-spacing: 0.3px;
  }
  .contact__role {
    font-size: 11px;
    color: var(--ink-soft);
    margin-top: 3px;
  }
  .contact__lines {
    list-style: none;
    margin-top: 18px;
    font-size: 11px;
    line-height: 1.55;
  }
  .contact__sep { margin: 0 5px; opacity: 0.7; }
</style>
</head>
<body>
<main class="canvas">
  <section class="card card--front" aria-label="Business card front">
    <div class="brand">
      <span class="brand__square"></span>
      <span class="brand__text">
        <span class="brand__name">Arcova</span>
        <span class="brand__tag">Immigration Law</span>
      </span>
    </div>
  </section>

  <section class="card card--back" aria-label="Business card back">
    <div class="brand">
      <span class="brand__square"></span>
      <span class="brand__text">
        <span class="brand__name">Arcova</span>
        <span class="brand__tag">Immigration Law</span>
      </span>
    </div>
    <div class="contact">
      <p class="contact__name">Daniel R. Whitcombe</p>
      <p class="contact__role">Managing Director</p>
      <ul class="contact__lines">
        <li>48-210 Harbourview Road West, Kingston, ON K7L 3N6</li>
        <li>0721-455-390<span class="contact__sep">|</span>d.whitcombe@arcovalaw.com</li>
        <li>www.arcovalaw.com</li>
      </ul>
    </div>
  </section>
</main>
</body>
</html>
```